New business card/stationary for a consulting company

I am looking for a clean and very professional looking business card for my consulting company as well as corresponding stationary. I am uploading our logo. I like simple and powerful for the feel. No graphics but I am open on everything else. Below is my contact information but would like the final to be in a version I can add my employees information into and print. Thank you.

Daniel Whitcombe
dan@fernlowadvisory.com
2837 North 9th Avenue, Summit Floor, Cedar Hollow, Wisconsin 60483
www.fernlowadvisory.com

Industry/Entity Type

Consulting

Contact Information for Business Card

Daniel Whitcombe
dan@fernlowadvisory.com
www.fernlowadvisory.com

Font styles to use
Serif
Sans Serif

Requirements
Must have
• Our logo and the business card details.
Nice to have
• our website www.fernlowadvisory.com

```html
<!DOCTYPE html>
<html lang="en">
<head>
<meta charset="utf-8">
<title>Fernlow Advisory – Business Card</title>
<link href="https://fonts.googleapis.com/css2?family=Open+Sans:wght@400;600;700&display=swap" rel="stylesheet">
<style>
  :root {
    --backdrop: #4a403b;
    --card: #111111;
    --card-edge: #1c1c1c;
    --ink-light: #ffffff;
    --ink-silver: #8c8c8c;
    --ink-dim: #6a6a6a;
    --divider: #9a9a9a;
  }
  * { margin: 0; padding: 0; box-sizing: border-box; }
  html, body {
    width: 1200px; height: 864px; overflow: hidden;
    background: var(--backdrop);
    font-family: "Open Sans", sans-serif;
  }
  .stage { position: relative; width: 1200px; height: 864px; }
  .card {
    position: absolute;
    width: 560px; height: 320px;
    background: var(--card);
    border: 1px solid var(--card-edge);
    border-radius: 3px;
  }
  .card--front { left: 50px; top: 90px; }
  .card--back { left: 590px; top: 454px; }

  .front-brand {
    position: absolute; left: 0; right: 0; top: 118px;
    display: flex; align-items: center; justify-content: center; gap: 14px;
  }
  .brand-square { width: 22px; height: 22px; background: var(--ink-silver); flex: none; }
  .front-brand__name {
    color: var(--ink-silver); font-size: 30px; font-weight: 400;
    letter-spacing: 1px; text-transform: uppercase;
  }
  .front-web {
    position: absolute; left: 0; right: 0; top: 188px; text-align: center;
    color: var(--ink-dim); font-size: 13px; letter-spacing: 6px;
  }

  .back-brand {
    position: absolute; left: 34px; top: 128px; width: 230px;
    display: flex; align-items: center; gap: 10px;
  }
  .back-brand .brand-square { background: var(--ink-light); width: 18px; height: 18px; }
  .back-brand__name {
    color: var(--ink-light); font-size: 18px; font-weight: 600;
    letter-spacing: 1px; text-transform: uppercase; white-space: nowrap;
  }
  .back-divider {
    position: absolute; left: 282px; top: 70px; width: 1px; height: 180px;
    background: linear-gradient(to bottom, transparent, var(--divider), transparent);
  }
  .contact {
    position: absolute; left: 302px; top: 92px; right: 16px; color: var(--ink-light);
  }
  .contact__name { font-size: 17px; font-weight: 700; letter-spacing: .5px; margin-bottom: 14px; white-space: nowrap; }
  .contact__address { font-size: 13px; line-height: 1.35; margin-bottom: 4px; }
  .contact__row { display: flex; align-items: center; gap: 7px; font-size: 13px; line-height: 1.45; white-space: nowrap; }
  .contact__row svg { width: 11px; height: 11px; fill: var(--ink-light); flex: none; }
</style>
</head>
<body>
<main class="stage">
  <section class="card card--front">
    <div class="front-brand">
      <span class="brand-square"></span>
      <span class="front-brand__name">Fernlow Advisory</span>
    </div>
    <p class="front-web">www.fernlowadvisory.com</p>
  </section>

  <section class="card card--back">
    <div class="back-brand">
      <span class="brand-square"></span>
      <span class="back-brand__name">Fernlow Advisory</span>
    </div>
    <div class="back-divider"></div>
    <div class="contact">
      <p class="contact__name">DANIEL WHITCOMBE</p>
      <p class="contact__address">2837 North 9th Avenue<br>Summit Floor, Cedar Hollow<br>Wisconsin 60483</p>
      <p class="contact__row">
        <svg viewBox="0 0 12 12" aria-hidden="true"><path d="M0 2h12v1L6 7 0 3z M0 4.5l6 4 6-4V10H0z"/></svg>
        dan@fernlowadvisory.com
      </p>
      <p class="contact__row">
        <svg viewBox="0 0 12 12" aria-hidden="true"><circle cx="6" cy="6" r="6"/></svg>
        www.fernlowadvisory.com
      </p>
    </div>
  </section>
</main>
</body>
</html>
```